International business needs a web page design

We need a web page design for a new service that our new "sub-company" of our existing company will offer. We are based in Denmark, and our new "sub-company" is called 'Velkari'. The service we offer is automated server configuration and In-Depth monitoring, and optional operations support. Our monitoring has a lot of graphs (like those seen here: https://velkari.example/ with either black or white background ) and the website needs to communicate a sense of Security/safety and that our customers can relax, because we have the full overview of their service and servers. The website should not be with black background.

We deliver low price, high quality and professional operations - which we can do, because we automate it and have people with 15+ years of experience doing so.

We have attached :
a file with our logo : velkari
a file showing the content of the frontage : frontpage
a file showing the content of the user page(for logged in users) : User page
a file showing the pop-up dialog "page" : CallToAction_route
a file showing the 3-steps for the frontpage : 3-step for frontpage

Target Market(s)

Chief Technological officers (CTO's) and Developers (small business, run by developers) - who needs professional IT operations.

Industry/Entity Type

Business

Coding

Coded - Design and coding required

Number of Pages Required

3 page

Requirements
Must have
• Frontpage :
• A lot of visualization(some with people too) rather than a lot of text
• A short, describing text on front page telling what people get
• 3 steps showing people how it works. (Could be presented in a video placed on top of a big front image or perhaps with all 3 steps/pictures shown at the same time or perhaps in a completely different way).
Nice to have
• A big front image(perhaps a person with a cellphone showing graphs and a "all okay" message) with a text and the 3-steps pictures/or video on top of it
• 3 boxes under the front image/top of the site showing what benefits people get from the service
Should not have
• Not a black/dark site

```html
<!DOCTYPE html>
<html lang="en">
<head>
<meta charset="utf-8">
<title>Velkari — Instant Server Setup &amp; In Depth Monitoring</title>
<link rel="stylesheet" href="https://fonts.googleapis.com/css2?family=Poppins:wght@400;500;600;700&family=Roboto:wght@400;500&display=swap">
<style>
:root{
  --navy:#2e3445;
  --navy-band:#303648;
  --navy-footer:#2a2f3d;
  --navy-bottom:#252a36;
  --blue:#1a9ad6;
  --orange:#f7941d;
  --white:#ffffff;
  --ink:#3a3d45;
  --muted:#8a8d93;
  --footer-text:#8c919c;
  --rail:#c9cbce;
}
*{margin:0;padding:0;box-sizing:border-box}
html,body{width:770px;height:1200px;overflow:hidden}
body{position:relative;background:var(--white);font-family:'Roboto',Arial,sans-serif;color:var(--ink)}
.abs{position:absolute}

/* header */
.site-header{left:0;top:0;width:770px;height:51px;background:var(--navy)}
.brand{display:flex;align-items:center;gap:6px;color:var(--white);font-family:'Poppins',Arial,sans-serif;font-weight:500}
.brand-dot{border-radius:50%;background:var(--blue)}
.header-brand{left:70px;top:7px}
.header-brand .brand-dot{width:36px;height:36px}
.header-brand .brand-name{font-size:24px;line-height:1}
.nav-link{top:20px;font-family:'Poppins',Arial,sans-serif;font-size:9.5px;color:var(--white);letter-spacing:.2px}
.nav-active-bar{left:390px;top:0;width:41px;height:3px;background:var(--blue)}
.btn-login{left:626px;top:12px;width:72px;height:25px;background:var(--blue);border-radius:2px;color:var(--white);font-family:'Poppins',Arial,sans-serif;font-size:10px;display:flex;align-items:center;justify-content:center}

/* hero */
.hero-photo{left:0;top:51px;width:770px;height:398px;
  background:linear-gradient(90deg,#5b6066 0%,#777a7c 30%,#7d7a74 50%,#3d4358 72%,#2c3347 100%)}
.hero-title-small{left:114px;top:133px;font-family:'Poppins',Arial,sans-serif;font-weight:700;font-size:34px;color:var(--white);line-height:1;letter-spacing:-.5px}
.hero-title-big{left:112px;top:172px;font-family:'Poppins',Arial,sans-serif;font-weight:600;font-size:50px;color:var(--white);line-height:1;letter-spacing:-1px}
.hero-tagline{left:114px;top:230px;font-family:'Poppins',Arial,sans-serif;font-weight:600;font-style:italic;font-size:12.5px;color:var(--white)}
.hero-copy{left:114px;top:254px;width:260px;font-size:9px;line-height:15px;color:var(--white)}
.btn-setup{left:114px;top:298px;width:87px;height:25px;background:var(--blue);color:var(--white);font-family:'Poppins',Arial,sans-serif;font-size:10px;display:flex;align-items:center;justify-content:center}
.btn-video{left:223px;top:298px;width:88px;height:26px;border:1px solid var(--white);border-radius:2px;color:var(--white);font-family:'Poppins',Arial,sans-serif;font-size:10px;display:flex;align-items:center;justify-content:center}

/* timeline */
.timeline-rail{left:92px;top:156px;width:4px;height:632px;background:var(--rail)}
.timeline-start{left:77px;top:139px;width:34px;height:34px;border-radius:50%;background:var(--blue);border:4px solid #3fb3e6}
.step-icon{left:72px;width:44px;height:44px;border-radius:50%;background:var(--blue)}
.step-icon svg{display:block}
.step-title{left:132px;font-family:'Poppins',Arial,sans-serif;font-weight:500;font-size:13px;color:var(--ink);line-height:18px}
.step-copy{left:132px;width:230px;font-size:8.7px;line-height:13px;color:var(--muted)}

/* device */
.device{left:458px;top:470px;width:198px;height:403px;border-radius:30px;background:#1b1c1f;border:2px solid #5a5c60}
.device-speaker{left:73px;top:22px;width:30px;height:2px;background:#555;border-radius:1px}
.device-camera{left:57px;top:20px;width:5px;height:5px;border-radius:50%;background:#444}
.device-screen{left:10px;top:43px;width:176px;height:312px;background:linear-gradient(160deg,#6a2a2a 0%,#3a3f48 45%,#1e2026 100%)}
.device-home{left:84px;top:362px;width:28px;height:28px;border-radius:50%;border:2px solid #444}

/* signup band */
.signup-band{left:0;top:908px;width:770px;height:54px;background:var(--navy-band)}
.band-brand{left:70px;top:916px}
.band-brand .brand-dot{width:38px;height:38px}
.band-brand .brand-name{font-size:26px;line-height:1}
.band-try{left:542px;top:929px;font-family:'Poppins',Arial,sans-serif;font-size:11px;color:var(--white)}
.btn-signup{left:623px;top:926px;width:76px;height:21px;background:var(--orange);color:var(--white);font-family:'Poppins',Arial,sans-serif;font-size:9px;display:flex;align-items:center;justify-content:center}

/* footer */
.site-footer{left:0;top:962px;width:770px;height:196px;background:var(--navy-footer)}
.footer-heading{top:987px;font-family:'Roboto',Arial,sans-serif;font-size:13px;color:var(--white)}
.footer-list{top:1021px;list-style:none;font-size:8.7px;color:var(--footer-text)}
.footer-list li{height:23.2px}
.social{top:1041px;width:24px;height:24px;border-radius:50%;border:1.5px solid #3c4253;background:#323848}
.social.is-active{border-color:var(--blue)}
.bottom-bar{left:0;top:1158px;width:770px;height:42px;background:var(--navy-bottom)}
.copyright{left:72px;top:1174px;font-size:9px;color:var(--white)}
.bottom-link{top:1174px;font-size:9px;color:var(--white)}
</style>
</head>
<body>

<header>
  <div class="abs site-header"></div>
  <div class="abs brand header-brand"><span class="brand-dot"></span><span class="brand-name">Velkari</span></div>
  <div class="abs nav-active-bar"></div>
  <nav>
    <span class="abs nav-link" style="left:398px">HOME</span>
    <span class="abs nav-link" style="left:470px">SERVICES</span>
    <span class="abs nav-link" style="left:557px">ABOUT US</span>
    <span class="abs btn-login">LOGIN</span>
  </nav>
</header>

<section class="hero">
  <div class="abs hero-photo" role="img" aria-label="Smiling businessman in a suit holding out a smartphone and giving a thumbs up, blurred street behind him"></div>
  <h1>
    <span class="abs hero-title-small">Welcome To</span>
    <span class="abs hero-title-big">Velkari</span>
  </h1>
  <p class="abs hero-tagline">Instant Server Setup &amp; In Depth Monitoring</p>
  <p class="abs hero-copy">Lorem ipsum dolor sit amet, consectetur adipiscing elit. Aliquam dapibus arcu</p>
  <span class="abs btn-setup">SETUP NOW</span>
  <span class="abs btn-video">WATCH VIDEO</span>
</section>

<div class="abs timeline-rail"></div>
<div class="abs timeline-start"></div>

<section class="features">
  <div class="abs step-icon" style="top:494px">
    <svg width="44" height="44" viewBox="0 0 44 44"><circle cx="22" cy="22" r="14" fill="none" stroke="#fff" stroke-width="2"/><path d="M14 22h16M24 17l6 5-6 5" fill="none" stroke="#fff" stroke-width="2"/></svg>
  </div>
  <h2 class="abs step-title" style="top:483px">ITS FAST &amp; EASY</h2>
  <p class="abs step-copy" style="top:505px">Lorem ipsum dolor sit amet, consectetur adipiscing elit. Aliquam dapibus arcu eu nisi ornare hendrerit. Duis euismod imperdiet purus, ac pharetra lorem dictum vel. Vestibulum at vestibulum ante.</p>

  <div class="abs step-icon" style="top:625px">
    <svg width="44" height="44" viewBox="0 0 44 44"><circle cx="22" cy="22" r="14" fill="none" stroke="#fff" stroke-width="2"/><path d="M15 22l5 5 9-10" fill="none" stroke="#fff" stroke-width="2.2"/></svg>
  </div>
  <h2 class="abs step-title" style="top:614px">RELAX &amp; REST ASSURED</h2>
  <p class="abs step-copy" style="top:636px">Lorem ipsum dolor sit amet, consectetur adipiscing elit. Aliquam dapibus arcu eu nisi ornare hendrerit. Duis euismod imperdiet purus, ac pharetra lorem dictum vel. Vestibulum at vestibulum ante.</p>

  <div class="abs step-icon" style="top:766px">
    <svg width="44" height="44" viewBox="0 0 44 44"><circle cx="22" cy="22" r="14" fill="none" stroke="#fff" stroke-width="2"/><path d="M14 28l5-6 4 3 7-9" fill="none" stroke="#fff" stroke-width="2"/></svg>
  </div>
  <h2 class="abs step-title" style="top:756px">YOU WILL LOVE YOUR DETAILED<br>PERFORMANCE GRAPHICS</h2>
  <p class="abs step-copy" style="top:796px">Lorem ipsum dolor sit amet, consectetur adipiscing elit. euismod imperdiet purus, ac pharetra lorem dictum vel. Vestibulum at vestibulum ante.</p>

  <div class="abs device">
    <div class="abs device-camera"></div>
    <div class="abs device-speaker"></div>
    <div class="abs device-screen" role="img" aria-label="Monitoring app screen showing line graphs and a volume bar chart over a hand reaching toward the display"></div>
    <div class="abs device-home"></div>
  </div>
</section>

<section class="signup">
  <div class="abs signup-band"></div>
  <div class="abs brand band-brand"><span class="brand-dot"></span><span class="brand-name">Velkari</span></div>
  <span class="abs band-try">TRY IT NOW</span>
  <span class="abs btn-signup">SIGNUP</span>
</section>

<footer>
  <div class="abs site-footer"></div>
  <h3 class="abs footer-heading" style="left:94px">Info</h3>
  <ul class="abs footer-list" style="left:94px">
    <li>Sign Up Now</li><li>Features</li><li>try it Now</li><li>Contact Us</li>
  </ul>
  <h3 class="abs footer-heading" style="left:197px">Email</h3>
  <ul class="abs footer-list" style="left:197px"><li>info@velkari.example</li></ul>
  <h3 class="abs footer-heading" style="left:309px">Company</h3>
  <ul class="abs footer-list" style="left:309px"><li>Careers</li></ul>
  <h3 class="abs footer-heading" style="left:422px">Contact Us</h3>
  <ul class="abs footer-list" style="left:422px">
    <li>Lorem Ipsum dolor sit amet</li><li>Consectetur</li><li>Adipsicing</li><li>Elit Sed Do</li><li>Call Us: 0155 010 2040</li>
  </ul>
  <span class="abs social is-active" style="left:555px"></span>
  <span class="abs social" style="left:585px"></span>
  <span class="abs social" style="left:618px"></span>
  <span class="abs social" style="left:650px"></span>

  <div class="abs bottom-bar"></div>
  <p class="abs copyright">Copyright © 2014 . All rights Reserved</p>
  <span class="abs bottom-link" style="left:572px">Home</span>
  <span class="abs bottom-link" style="left:607px">About Us</span>
  <span class="abs bottom-link" style="left:656px">Contact Us</span>
</footer>

</body>
</html>
```